Bref créative
Brookmere
Brookmere Vale Baptist Church
Simple
Dolores Lomax
Communications
4163 Ambervale Road
Regina SK S7N 3K8
dolores@brookmerechapel.ca
brookmerechapel.ca
We will need business cards, letterhead and envelopes.
Our Logo
ai file

```html
<!DOCTYPE html>
<html lang="en">
<head>
<meta charset="utf-8">
<title>Brookmere Vale Baptist Church — Stationery</title>
<link rel="stylesheet" href="https://fonts.googleapis.com/css2?family=Cinzel:wght@500&family=Open+Sans:wght@400;600&display=swap">
<style>
:root{
  --bg:#e8e5e0;
  --paper:#ffffff;
  --blue-dark:#17507f;
  --blue:#2a73ab;
  --blue-light:#6fa6cf;
  --gold:#b9aa72;
  --gold-dark:#8e7f4a;
  --ink:#5a5f66;
  --faint:#e3ecf3;
}
*{margin:0;padding:0;box-sizing:border-box}
html,body{width:1200px;height:497px;overflow:hidden}
body{background:var(--bg);position:relative;font-family:"Open Sans",Arial,sans-serif;color:var(--ink)}
.piece{position:absolute;background:var(--paper);box-shadow:0 2px 6px rgba(0,0,0,.18);overflow:hidden}
.wave{position:absolute;inset:0;width:100%;height:100%}
.brand{position:absolute;text-align:left;white-space:nowrap}
.brand-name{font-family:"Cinzel",Georgia,serif;font-weight:500;color:var(--blue);letter-spacing:1px;line-height:1}
.brand-tag{font-size:5px;color:var(--gold-dark);letter-spacing:.5px;margin-top:2px}
.on-dark .brand-name{color:#fff}
.on-dark .brand-tag{color:#dfe9f2}
.on-gold .brand-name{color:#fff}
.on-gold .brand-tag{color:#fff}
.contact{position:absolute;font-size:4.6px;line-height:1.5;color:var(--ink);white-space:nowrap}
.contact .who{font-weight:600;font-size:5.6px;color:var(--blue-dark)}
.contact .role{color:var(--gold-dark);margin-bottom:3px}
.on-dark .contact{color:#fff}
.on-dark .contact .who,.on-dark .contact .role{color:#fff}
.card{width:124px;height:70px}
.card-front-a{left:18px;top:60px;background:var(--blue)}
.card-back-a{left:152px;top:60px}
.card-back-a .contact{left:5px;top:8px;font-size:4px;color:#fff}
.card-back-a .contact .who{font-size:5px;color:#fff}
.card-back-a .contact .role{color:#fff}
.card-back-a .brand{left:62px;top:20px}
.card-back-a .brand-name{font-size:8.5px;letter-spacing:.3px}
.card-back-a .brand-tag{font-size:2.6px;letter-spacing:.2px}
.card-front-b{left:18px;top:140px;background:var(--blue)}
.card-back-b{left:152px;top:140px}
.card-gold{left:85px;top:220px;background:var(--gold)}
.letterhead{left:300px;top:22px;width:330px;height:456px}
.letterhead .contact{right:24px;top:30px;font-size:5.5px;text-align:left}
.letterhead .mark{position:absolute;left:110px;top:160px;width:110px;height:110px;border-radius:50%;background:var(--faint)}
.envelope{width:380px;height:140px;left:700px}
.env-back{top:22px;background:#f4f4f2}
.env-plain{top:178px}
.env-blue{top:334px}
.envelope .mark{position:absolute;right:40px;top:40px;width:60px;height:60px;border-radius:50%;background:var(--faint)}
</style>
</head>
<body>

<div class="piece card card-front-a on-dark">
  <svg class="wave" viewBox="0 0 124 70" preserveAspectRatio="none" aria-hidden="true">
    <path d="M80 0 C95 25 70 45 90 70 L124 70 L124 0 Z" fill="#fff"/>
  </svg>
  <div class="contact" style="left:8px;top:8px">
    <div class="who">Dolores Lomax</div>
    <div class="role">Communications</div>
    <div>4163 Ambervale Road</div>
    <div>Regina SK S7N 3K8</div>
    <div>Tel (306) 555-0187</div>
    <div>dolores@brookmerechapel.ca</div>
  </div>
</div>

<div class="piece card card-back-a">
  <svg class="wave" viewBox="0 0 124 70" preserveAspectRatio="none" aria-hidden="true">
    <defs><linearGradient id="gA" x1="0" x2="1"><stop offset="0" stop-color="#2a73ab"/><stop offset="1" stop-color="#17507f"/></linearGradient></defs>
    <path d="M0 0 L58 0 C48 30 66 50 52 70 L0 70 Z" fill="url(#gA)"/>
  </svg>
  <div class="contact">
    <div class="who">Dolores Lomax</div>
    <div class="role">Communications</div>
    <div>brookmerechapel.ca</div>
  </div>
  <div class="brand">
    <div class="brand-name">Brookmere</div>
    <div class="brand-tag">Brookmere Vale Baptist Church</div>
  </div>
</div>

<div class="piece card card-front-b on-dark">
  <svg class="wave" viewBox="0 0 124 70" preserveAspectRatio="none" aria-hidden="true">
    <path d="M0 52 C40 44 80 66 124 50 L124 70 L0 70 Z" fill="#17507f"/>
  </svg>
  <div class="brand" style="left:14px;top:24px">
    <div class="brand-name" style="font-size:16px">Brookmere</div>
    <div class="brand-tag" style="font-size:4.2px">Brookmere Vale Baptist Church</div>
  </div>
</div>

<div class="piece card card-back-b">
  <div class="brand" style="left:14px;top:24px">
    <div class="brand-name" style="font-size:16px">Brookmere</div>
    <div class="brand-tag" style="font-size:4.2px">Brookmere Vale Baptist Church</div>
  </div>
</div>

<div class="piece card card-gold on-gold">
  <div class="brand" style="left:14px;top:24px">
    <div class="brand-name" style="font-size:16px">Brookmere</div>
    <div class="brand-tag" style="font-size:4.2px">Brookmere Vale Baptist Church</div>
  </div>
</div>

<div class="piece letterhead">
  <svg class="wave" viewBox="0 0 330 456" preserveAspectRatio="none" aria-hidden="true">
    <path d="M0 420 C60 430 110 456 150 456 L0 456 Z" fill="#2a73ab"/>
  </svg>
  <div class="brand" style="left:24px;top:28px">
    <div class="brand-name" style="font-size:24px">Brookmere</div>
    <div class="brand-tag" style="font-size:6px">Brookmere Vale Baptist Church</div>
  </div>
  <div class="contact">
    <div>4163 Ambervale Road</div>
    <div>Regina SK S7N 3K8</div>
    <div>Tel (306) 555-0187</div>
    <div>Fax (306) 555-0188</div>
    <div>brookmerechapel.ca</div>
  </div>
  <div class="mark"></div>
</div>

<div class="piece envelope env-back">
  <svg class="wave" viewBox="0 0 380 140" preserveAspectRatio="none" aria-hidden="true">
    <path d="M0 0 L380 0 L200 80 Q190 85 180 80 Z" fill="#b9aa72"/>
    <path d="M0 0 L180 80 Q190 85 200 80 L380 0" fill="none" stroke="#8e7f4a" stroke-width="1"/>
  </svg>
</div>

<div class="piece envelope env-plain">
  <div class="brand" style="left:16px;top:14px">
    <div class="brand-name" style="font-size:14px">Brookmere</div>
    <div class="brand-tag" style="font-size:4px">Brookmere Vale Baptist Church</div>
  </div>
  <div class="contact" style="left:16px;top:42px">
    <div>4163 Ambervale Road</div>
    <div>Regina SK S7N 3K8</div>
  </div>
  <div class="mark"></div>
</div>

<div class="piece envelope env-blue">
  <svg class="wave" viewBox="0 0 380 140" preserveAspectRatio="none" aria-hidden="true">
    <defs><linearGradient id="gE" x1="0" x2="1"><stop offset="0" stop-color="#17507f"/><stop offset="1" stop-color="#2a73ab"/></linearGradient></defs>
    <path d="M0 0 L380 0 L380 18 C260 40 150 10 0 42 Z" fill="url(#gE)"/>
  </svg>
  <div class="brand" style="left:16px;top:52px">
    <div class="brand-name" style="font-size:14px">Brookmere</div>
    <div class="brand-tag" style="font-size:4px">Brookmere Vale Baptist Church</div>
  </div>
  <div class="contact" style="left:16px;top:80px">
    <div>4163 Ambervale Road</div>
    <div>Regina SK S7N 3K8</div>
    <div>brookmerechapel.ca</div>
  </div>
  <div class="mark"></div>
</div>

</body>
</html>
```